New custom software business needs a Wordpress site

We need a Wordpress site for a new company based out of Chicago called 'Vellora Consulting'. Using a mix of on and off-shore resources we build custom software solutions, mainly focusing on small to medium sized companies. We help our customers "aspire" to do great things.
We have a basic site up here: https://brindlewave.example/. We worked on the content for it but not the branding. For now, this houses all the pages (except for a Contact Us page we'll be adding soon) for the foreseeable future.
We also have a new logo (attached) that we'd like to base the styling/colors on.
Target Market(s)
Small to medium sized companies that require tech resources
Industry/Entity Type
Software
Nice to have
- Teamwork, tech, professional but not elitist

```html
<!DOCTYPE html>
<html lang="en">
<head>
<meta charset="utf-8">
<title>Vellora Consulting</title>
<link href="https://fonts.googleapis.com/css2?family=Montserrat:ital,wght@0,400;0,500;0,600;0,700;1,500;1,600&family=Orbitron:wght@400;500&display=swap" rel="stylesheet">
<style>
:root{
  --blue:#0b57b8;
  --blue-dark:#0a4aa3;
  --blue-light:#1f74d6;
  --navy:#0a1036;
  --ink:#1c2233;
  --text:#555b66;
  --mist:#e8eef7;
  --rule:#d6dbe3;
  --white:#ffffff;
}
*{margin:0;padding:0;box-sizing:border-box}
html,body{width:1200px;height:3985px;overflow:hidden}
body{position:relative;font-family:'Montserrat',sans-serif;color:var(--ink);background:var(--white)}
.abs{position:absolute}
.display{font-family:'Orbitron',sans-serif;font-weight:400;letter-spacing:2px;text-transform:uppercase}
.btn{position:absolute;display:flex;align-items:center;justify-content:center;border-radius:40px;background:linear-gradient(90deg,var(--blue-dark),var(--blue-light));color:var(--white);font-weight:600;font-size:18px;letter-spacing:.3px}

/* hero */
.hero{position:absolute;left:0;top:0;width:1200px;height:667px;background:linear-gradient(180deg,#4f6274 0%,#8b99a6 35%,#6a737c 70%,#3f4650 100%)}
.hero-shade{position:absolute;inset:0;background:linear-gradient(180deg,rgba(10,20,40,.35),rgba(10,20,40,.1) 60%,rgba(10,20,40,.25))}
.brand{left:111px;top:52px;color:var(--white);font-weight:600;font-size:28px;letter-spacing:1px;line-height:1}
.brand small{display:block;font-size:13px;letter-spacing:3px;margin-top:6px;font-weight:600}
.nav{right:111px;top:63px;display:flex;gap:26px;color:var(--white);font-weight:600;font-size:18px}
.hero-title{left:0;width:1200px;top:206px;text-align:center;color:var(--white);font-size:58px;line-height:64px;letter-spacing:3px}
.hero-sub{left:290px;width:620px;top:354px;text-align:center;color:var(--white);font-size:22px;line-height:33px}

/* about */
.about-photo{left:111px;top:747px;width:436px;height:442px;background:linear-gradient(135deg,#8d8a84,#c9c5bd 45%,#6d7b8c)}
.about-title{left:632px;top:758px;font-size:34px;line-height:46px;color:var(--ink)}
.about-copy{left:632px;top:876px;width:460px;font-size:16.5px;line-height:25px;color:var(--text)}
.about-copy p+p{margin-top:25px}

/* services */
.services{left:0;top:1276px;width:1200px;height:587px;background:var(--mist)}
.sec-title{left:0;width:1200px;text-align:center;font-size:34px;color:var(--ink)}
.svc{width:300px}
.svc h3{font-size:23px;line-height:33px;font-weight:600;color:var(--ink);margin-top:26px}
.svc p{font-size:16.5px;line-height:25px;color:var(--text);margin-top:20px}
.svc-deco{left:420px;top:1400px;width:360px;height:400px;background:radial-gradient(ellipse at center,rgba(70,120,170,.35),rgba(70,120,170,0) 70%)}

/* why */
.why-col{top:2028px;width:243px;height:240px;text-align:center}
.why-col h4{position:absolute;left:0;right:0;top:135px;font-size:23px;line-height:30px;font-weight:600;color:var(--ink)}
.why-col svg{position:absolute;left:50%;top:26px;transform:translateX(-50%)}
.divider{width:1px;top:2028px;height:240px;background:var(--rule)}

/* testimonials */
.testi{left:0;top:2319px;width:1200px;height:498px;background:linear-gradient(120deg,#0a4aa3 0%,#155fc0 60%,#2a7ad6 100%)}
.quote{left:200px;width:800px;top:2476px;text-align:center;color:var(--white);font-style:italic;font-weight:500;font-size:24.5px;line-height:36px}
.avatar{border-radius:50%;background:linear-gradient(160deg,#c8b8a8,#7a6556)}
.testi-name{left:0;width:1200px;top:2712px;text-align:center;color:var(--white);font-weight:600;font-size:20px}
.testi-role{left:0;width:1200px;top:2740px;text-align:center;color:var(--white);font-size:17px}

/* leadership */
.leader-photo{top:2953px;width:223px;height:223px;border-radius:50%}
.leader{top:3208px;width:480px;text-align:center}
.leader h3{font-size:22px;font-weight:500;color:#4a4f5a}
.leader p{margin-top:16px;font-size:16px;line-height:23.3px;color:var(--text)}

/* footer */
.footer{left:0;top:3567px;width:1200px;height:418px;background:var(--navy);color:var(--white)}
.foot-brand{left:111px;top:3775px;font-weight:600;font-size:40px;letter-spacing:1px;line-height:1}
.foot-brand small{display:block;font-size:17px;letter-spacing:4px;margin-top:10px;color:#5c9be6;font-weight:600}
.foot-col h5{font-size:20px;font-weight:600;margin-bottom:20px}
.foot-col li{list-style:none;font-size:16.5px;line-height:29px}
.contact-row{display:flex;gap:10px;font-size:16.5px;line-height:29px}
.contact-row svg{flex:none;margin-top:7px}
.rule{left:111px;top:3876px;width:978px;height:1px;background:rgba(255,255,255,.2)}
.copyright{left:111px;top:3919px;font-size:16px}
.social{left:1047px;top:3910px;width:40px;height:40px;border-radius:50%;border:1.5px solid #5c9be6}
</style>
</head>
<body>

<!-- Hero -->
<section class="hero" role="img" aria-label="Photo of downtown city skyscrapers under a cloudy sky">
  <div class="hero-shade"></div>
</section>
<div class="abs brand">VELLORA<small>CONSULTING</small></div>
<nav class="abs nav"><span>Services</span><span>Why Vellora?</span><span>Vellora Leadership</span><span>Contact Us</span></nav>
<h1 class="abs display hero-title">Custom Software<br>Business</h1>
<p class="abs hero-sub">A software consulting company specializing in serving small to medium size businesses</p>
<div class="btn" style="left:505px;top:447px;width:191px;height:62px;font-size:20px">LET’S TALK</div>

<!-- About -->
<div class="abs about-photo" role="img" aria-label="Photo of a team meeting with colleagues shaking hands around a table"></div>
<h2 class="abs display about-title">Welcome to<br>Vellora Consulting</h2>
<div class="abs about-copy">
  <p>A software consulting company specializing in serving small to medium size businesses. We understand the unique challenges and opportunities that these companies face, and we are dedicated to helping them succeed through innovative technology solutions.</p>
  <p>Our team of experienced professionals has a diverse range of skills and expertise, making us well-equipped to handle any project, big or small.</p>
</div>
<div class="btn" style="left:632px;top:1133px;width:174px;height:59px">READ MORE</div>

<!-- Services -->
<section class="abs services"></section>
<h2 class="abs display sec-title" style="top:1336px">Services</h2>
<div class="abs svc-deco" role="img" aria-label="Soft blue decorative backdrop"></div>

<div class="abs svc" style="left:111px;top:1412px">
  <svg width="90" height="100" viewBox="0 0 90 100" fill="none" stroke="#0b57b8" stroke-width="2.5" stroke-linecap="round">
    <path d="M45 18a26 26 0 0 0-15 47v10h30V65a26 26 0 0 0-15-47z"/>
    <path d="M34 82h22M36 89h18"/>
    <circle cx="45" cy="40" r="7"/><path d="M45 47v20M45 58h6M45 63h5"/>
    <path d="M45 4v7M14 14l5 5M76 14l-5 5M4 42h7M79 42h7"/>
  </svg>
  <h3>Custom Solution<br>Delivery</h3>
  <p>Vellora offers a range of services focused on helping businesses and organizations deliver software solutions to their customers or users.</p>
  <svg style="margin-top:22px" width="30" height="12" viewBox="0 0 30 12"><path d="M0 6h26M21 1l6 5-6 5" fill="none" stroke="#1c2233" stroke-width="2.5"/></svg>
</div>

<div class="abs svc" style="left:807px;top:1412px">
  <svg width="104" height="100" viewBox="0 0 104 100" fill="none" stroke="#0b57b8" stroke-width="2.5" stroke-linecap="round">
    <path d="M20 48V10M14 16l6-6 6 6M52 58V8M46 14l6-6 6 6M84 48V10M78 16l6-6 6 6" stroke-dasharray="4 4"/>
    <circle cx="20" cy="62" r="7"/><path d="M6 86a14 14 0 0 1 28 0z"/>
    <circle cx="84" cy="62" r="7"/><path d="M70 86a14 14 0 0 1 28 0z"/>
    <circle cx="52" cy="72" r="7"/><path d="M38 96a14 14 0 0 1 28 0z"/>
  </svg>
  <h3>Staff<br>Augmentation</h3>
  <p>Let Vellora help you supplement your existing software development teams with additional resources and expertise. We provided access to experienced</p>
  <svg style="margin-top:22px" width="30" height="12" viewBox="0 0 30 12"><path d="M0 6h26M21 1l6 5-6 5" fill="none" stroke="#1c2233" stroke-width="2.5"/></svg>
</div>

<!-- Why -->
<h2 class="abs display sec-title" style="top:1928px">Why Vellora Consulting?</h2>

<div class="abs why-col" style="left:87px">
  <svg width="92" height="92" viewBox="0 0 92 92" fill="none" stroke="#0b57b8" stroke-width="2.5" stroke-linecap="round">
    <rect x="4" y="4" width="64" height="70" rx="3"/><path d="M4 14h64"/>
    <path d="M12 24h10M12 32h10M12 40h10M12 48h10"/>
    <path d="M36 30l-5 5 5 5M48 30l5 5-5 5M44 28l-4 14"/>
    <circle cx="66" cy="66" r="20" fill="#fff"/><path d="M57 66l6 6 12-12"/>
  </svg>
  <h4>High-quality<br>software solution</h4>
</div>
<div class="abs divider" style="left:356px"></div>
<div class="abs why-col" style="left:357px">
  <svg width="84" height="92" viewBox="0 0 84 92" fill="none" stroke="#0b57b8" stroke-width="2.5" stroke-linecap="round">
    <path d="M20 88V70C8 62 4 50 6 38 9 16 28 4 48 6c20 3 32 20 30 38l6 12h-8v14c0 6-4 8-10 8h-8v10"/>
    <circle cx="42" cy="40" r="14"/><circle cx="42" cy="40" r="5"/>
    <path d="M42 18v8M42 54v8M20 40h8M56 40h8M28 26l5 5M51 49l5 5M56 26l-5 5M28 54l5-5"/>
  </svg>
  <h4>Technical<br>expertise</h4>
</div>
<div class="abs divider" style="left:600px"></div>
<div class="abs why-col" style="left:601px">
  <svg width="92" height="92" viewBox="0 0 92 92" fill="none" stroke="#0b57b8" stroke-width="2.5" stroke-linecap="round">
    <path d="M46 4l6 8 10-3 2 10 10 2-3 10 8 6-8 6 3 10-10 2-2 10-10-3-6 8-6-8-10 3-2-10-10-2 3-10-8-6 8-6-3-10 10-2 2-10 10 3z"/>
    <circle cx="46" cy="46" r="24"/><path d="M46 30v16l10 6"/>
  </svg>
  <h4>Delivering<br>excellence</h4>
</div>
<div class="abs divider" style="left:843px"></div>
<div class="abs why-col" style="left:868px">
  <svg width="104" height="92" viewBox="0 0 104 92" fill="none" stroke="#0b57b8" stroke-width="2.5" stroke-linejoin="round">
    <circle cx="52" cy="16" r="12"/><path d="M28 50a24 22 0 0 1 48 0z"/><path d="M46 30l6 8 6-8"/>
    <path d="M16 62l3 7 8 1-6 5 2 8-7-4-7 4 2-8-6-5 8-1z"/>
    <path d="M52 62l3 7 8 1-6 5 2 8-7-4-7 4 2-8-6-5 8-1z"/>
    <path d="M88 62l3 7 8 1-6 5 2 8-7-4-7 4 2-8-6-5 8-1z"/>
  </svg>
  <h4>Customer<br>Satisfaction</h4>
</div>

<!-- Testimonials -->
<section class="abs testi"></section>
<h2 class="abs display sec-title" style="top:2388px;color:var(--white)">Client Testimonials</h2>
<svg class="abs" style="left:110px;top:2525px" width="20" height="32" viewBox="0 0 20 32"><path d="M16 3L4 16l12 13" fill="none" stroke="#9cc4f2" stroke-width="3"/></svg>
<svg class="abs" style="left:1070px;top:2525px" width="20" height="32" viewBox="0 0 20 32"><path d="M4 3l12 13L4 29" fill="none" stroke="#9cc4f2" stroke-width="3"/></svg>
<p class="abs quote">“ Duis aute irure dolor in reprehenderit in voluptate velit esse cillum dolore eu fugiat nulla pariatur. Excepteur sint occaecat cupidatat non proidenttat sunt in culp ”</p>
<div class="abs avatar" style="left:558px;top:2614px;width:84px;height:84px;border:3px solid #fff" role="img" aria-label="Portrait of the client giving the testimonial"></div>
<div class="abs testi-name">Dean Porter</div>
<div class="abs testi-role">Lorem ipisum edhfeyu</div>

<!-- Leadership -->
<h2 class="abs display sec-title" style="top:2878px">Vellora Leadership</h2>
<div class="abs leader-photo" style="left:209px;background:linear-gradient(160deg,#a9b4bf,#6b7886)" role="img" aria-label="Portrait of Elliot, company leader"></div>
<div class="abs leader-photo" style="left:750px;background:linear-gradient(160deg,#d9dcde,#1f3b4f)" role="img" aria-label="Portrait of Ravi, company leader"></div>

<div class="abs leader" style="left:80px">
  <h3>Elliot</h3>
  <p>As a leader, Elliot is dedicated to fostering a culture of collaboration, innovation, and excellence within his team. He believes that by empowering his team members and encouraging open communication, he can create an environment that is conducive to creativity and problem-solving.</p>
</div>
<div class="abs leader" style="left:621px">
  <h3>Ravi</h3>
  <p>As a leader, Ravi is dedicated to fostering a culture of collaboration, innovation, and excellence within his team. He believes that by empowering his team members and encouraging open communication, he can create an environment that is conducive to creativity and problem-solving.</p>
</div>
<div class="btn" style="left:234px;top:3418px;width:174px;height:59px">READ MORE</div>
<div class="btn" style="left:775px;top:3418px;width:174px;height:59px">READ MORE</div>

<!-- Footer -->
<footer class="abs footer"></footer>
<div class="abs foot-brand">VELLORA<small>CONSULTING</small></div>

<div class="abs foot-col" style="left:461px;top:3615px;color:#fff">
  <h5>Quick Links</h5>
  <ul><li>Home</li><li>About</li><li>Services</li><li>Why Vellora?</li><li>Vellora Leadership</li><li>Contact Us</li></ul>
</div>

<div class="abs foot-col" style="left:700px;top:3615px;color:#fff">
  <h5>Contact Us</h5>
  <div class="contact-row">
    <svg width="10" height="14" viewBox="0 0 10 14"><path d="M5 0a5 5 0 0 0-5 5c0 4 5 9 5 9s5-5 5-9a5 5 0 0 0-5-5zm0 7a2 2 0 1 1 0-4 2 2 0 0 1 0 4z" fill="#5c9be6"/></svg>
    <span>4800 W. Harbor Avenue, Suite 210,<br>Chicago IL 60601</span>
  </div>
  <div class="contact-row" style="margin-top:29px">
    <svg width="12" height="12" viewBox="0 0 12 12"><path d="M2.5 0l2 3-1.3 1.5a7 7 0 0 0 4.3 4.3L9 7.5l3 2-1.5 2.5C5 12 0 7 0 1.5z" fill="#5c9be6"/></svg>
    <span>1 555 010 2020</span>
  </div>
  <div class="contact-row" style="margin-top:29px">
    <svg width="15" height="11" viewBox="0 0 15 11"><rect width="15" height="11" rx="1" fill="#5c9be6"/><path d="M1 1l6.5 5L14 1" fill="none" stroke="#0a1036" stroke-width="1.3"/></svg>
    <span>hello@velloraconsulting.example</span>
  </div>
</div>

<div class="abs rule"></div>
<div class="abs copyright">© Copyright 2022 Vellora Consulting. All Rights Reserved.</div>
<div class="abs social" aria-label="Social profile"></div>

</body>
</html>
```